Magnetic Business card Design do a service provider

Hi,

The company aim is to provide all service needs under one roof. However, at the moment there is only Accounting, Electrical and IT branches. There will be more services coming onboard in the future.

I already have a logo designed (Company name is already part of the logo), I now need a magnetic business card designed.

The business card will contain the following:

- Company Logo
- Contact#
- E-mail
- enough space to add website URL (for future)
Updates

Project Deadline Extended Reason: HI All,The deadline has been extended due to not having enough time to review an overwhelming number of designs that has been submitted by lots of designers.I will be uploading a draft of designs that i have in mind.Thanks. Added Friday, January 22, 2016

Target Market(s)

Residential, Home-based Businesses, Small and Medium businesses

Industry/Entity Type

Business

Contact Information for Business Card

Contact#: 0491 738 520
E-mail: service@brightlanetrades.net.au

Font styles to use
Decorative
Script

Requirements
Must have
• Round edges
• Some form of logo incorporation as a background

```html
<!DOCTYPE html>
<html lang="en">
<head>
<meta charset="utf-8">
<title>Bright Lane Trades – Business Card</title>
<link href="https://fonts.googleapis.com/css2?family=Open+Sans:wght@400;600;700&display=swap" rel="stylesheet">
<style>
  :root {
    --page: #e9e6e1;
    --brand-blue: #1d5fa8;
    --deep-blue: #164f92;
    --sky-blue: #5bbbe8;
    --silver: #a7a9ac;
    --white: #ffffff;
  }
  * { margin: 0; padding: 0; box-sizing: border-box; }
  html, body {
    width: 1200px; height: 950px; overflow: hidden;
    background: var(--page);
    font-family: "Open Sans", Arial, sans-serif;
  }
  .canvas { position: relative; width: 1200px; height: 950px; }

  .card {
    position: absolute;
    width: 560px; height: 340px;
    border-radius: 18px;
    overflow: hidden;
    box-shadow: 0 10px 28px rgba(0,0,0,0.22);
  }

  /* Front side */
  .card-front {
    left: 80px; top: 100px;
    background: linear-gradient(135deg, #2a6cb5 0%, var(--brand-blue) 55%, var(--deep-blue) 100%);
  }
  .front-backdrop { position: absolute; inset: 0; }
  .front-brand {
    position: absolute; left: 0; right: 0; top: 128px;
    text-align: center; color: var(--white);
  }
  .front-name { font-size: 34px; font-weight: 600; letter-spacing: 0.5px; }
  .front-url { margin-top: 10px; font-size: 17px; font-weight: 400; letter-spacing: 1.5px; }

  /* Back side */
  .card-back { left: 560px; top: 480px; background: var(--white); }
  .card-wave { position: absolute; inset: 0; }
  .person {
    position: absolute; right: 40px; top: 34px; text-align: right;
  }
  .person-name { color: var(--brand-blue); font-size: 21px; font-weight: 600; letter-spacing: 0.5px; }
  .person-role { color: var(--sky-blue); font-size: 15px; font-weight: 600; margin-top: 2px; }

  .brand-mark {
    position: absolute; left: 34px; top: 150px;
    display: flex; align-items: center; gap: 12px;
  }
  .brand-dot { width: 30px; height: 30px; border-radius: 50%; background: var(--brand-blue); }
  .brand-name { color: var(--brand-blue); font-size: 27px; font-weight: 600; }

  .contact {
    position: absolute; right: 36px; top: 212px; text-align: right; color: var(--white);
  }
  .contact-phone { font-size: 22px; font-weight: 700; letter-spacing: 0.5px; margin-bottom: 6px; }
  .contact-line { font-size: 13px; font-weight: 400; line-height: 1.5; }
</style>
</head>
<body>
<main class="canvas">

  <section class="card card-front" aria-label="Business card front">
    <div class="front-backdrop" role="img" aria-label="Faint repeated brand emblem pattern across the blue background"></div>
    <div class="front-brand">
      <div class="front-name">Bright Lane Trades</div>
      <div class="front-url">brightlanetrades.net.au</div>
    </div>
  </section>

  <section class="card card-back" aria-label="Business card back">
    <svg class="card-wave" width="560" height="340" viewBox="0 0 560 340" aria-hidden="true">
      <path d="M0,288 C150,282 250,262 320,222 C400,175 440,110 560,92 L560,106 C450,124 420,190 345,238 C275,282 160,300 0,302 Z" fill="var(--sky-blue)"/>
      <path d="M0,308 C150,304 260,290 335,250 C410,202 445,128 560,114 L560,340 L0,340 Z" fill="var(--brand-blue)"/>
      <path d="M0,316 C150,314 250,302 330,272 L330,284 C250,312 150,326 0,330 Z" fill="var(--silver)"/>
    </svg>

    <div class="person">
      <div class="person-name">DANIEL HARPER</div>
      <div class="person-role">CEO/FOUNDER</div>
    </div>

    <div class="brand-mark">
      <span class="brand-dot"></span>
      <span class="brand-name">Bright Lane Trades</span>
    </div>

    <div class="contact">
      <div class="contact-phone">0491 738 520</div>
      <div class="contact-line">service@brightlanetrades.net.au</div>
      <div class="contact-line">www.brightlanetrades.net.au</div>
    </div>
  </section>

</main>
</body>
</html>
```